Bref créative
Stationery - Business Card / Letterhead
For Public Adjusting Company
Professional
Doran T. Whitcombe
Sr. Public Adjuster
58 W. Alder St.
Suite 612
Alder Falls, NY 11492
doran@trclaimpro.com
www.trclaimpro.com
On the front I want our logo with the shadow on the bottom
On the back I would like you to incorporate a little creative usage of either the shield/lighthouse logo and all of my information
This logo should be used as the front as it has the bottom shadow which for some reason is not showing up on the other logos
the business card front will be high gloss finish
Also the fax number should be 516.843.9075 not 829. there is no where else for me to edit that once the project is uploaded

```html
<!DOCTYPE html>
<html lang="en">
<head>
<meta charset="utf-8">
<title>TR Claim Advisors – Stationery</title>
<link href="https://fonts.googleapis.com/css2?family=Cinzel:wght@600&family=Libre+Baskerville:wght@400&display=swap" rel="stylesheet">
<style>
  :root{
    --navy:#0b2a58;
    --blue:#1d58a6;
    --blue-deep:#0e3470;
    --red:#c4202e;
    --paper:#ffffff;
    --ground:#e7e3de;
    --shadow:rgba(0,0,0,.18);
    --ink:#3a3f4a;
  }
  *{box-sizing:border-box;margin:0;padding:0}
  html,body{width:1200px;height:891px;overflow:hidden;background:var(--ground)}
  .stage{position:relative;width:1200px;height:891px}
  .piece{position:absolute;background:var(--paper);box-shadow:0 4px 14px var(--shadow);overflow:hidden}
  .brand{display:flex;align-items:center;gap:8px;font-family:"Cinzel",serif;font-weight:600;color:var(--red);white-space:nowrap;line-height:1}
  .brand-mark{display:block;flex:none;background:var(--navy)}
  .fine{font-family:"Libre Baskerville",serif;color:#fff;white-space:nowrap;line-height:1.2}

  .logo-card{left:0;top:80px;width:290px;height:111px;border-radius:0 14px 14px 0;display:flex;align-items:center;padding-left:40px;z-index:1}
  .logo-card .brand{font-size:20px}
  .logo-card .brand-mark{width:22px;height:22px}

  .letterhead{left:449px;top:80px;width:488px;height:693px;z-index:1}
  .letterhead .brand{position:absolute;left:36px;top:28px;font-size:16px}
  .letterhead .brand-mark{width:17px;height:17px}
  .letterhead .band{position:absolute;left:0;right:0;bottom:0;height:26px;background:linear-gradient(90deg,var(--navy),var(--blue-deep));border-top:2px solid var(--red);display:flex;align-items:center;justify-content:center}
  .letterhead .fine{font-size:7.5px}

  .envelope-back{left:48px;top:302px;width:392px;height:258px;z-index:2}
  .envelope-back svg{position:absolute;inset:0}

  .envelope-front{left:150px;top:447px;width:533px;height:236px;z-index:3}
  .envelope-front .brand{position:absolute;left:34px;top:40px;font-size:15px}
  .envelope-front .brand-mark{width:16px;height:16px}
  .envelope-front .band{position:absolute;left:0;right:0;bottom:0;height:22px;background:linear-gradient(90deg,var(--navy),var(--blue));border-top:2px solid var(--red);display:flex;align-items:center;justify-content:center}
  .envelope-front .fine{font-size:7px}

  .card-back{left:951px;top:521px;width:147px;height:124px;background:radial-gradient(circle at 50% 45%,var(--blue) 0%,var(--navy) 80%);display:flex;align-items:center;justify-content:center;z-index:1}
  .card-back .brand-mark{width:18px;height:18px;background:var(--paper)}

  .card-front{left:951px;top:647px;width:147px;height:121px;z-index:1}
  .card-front .person{position:absolute;right:14px;top:16px;text-align:center;font-family:"Libre Baskerville",serif;color:var(--ink)}
  .card-front .name{font-size:8px}
  .card-front .role{font-size:5.5px;margin-top:2px}
  .card-front .brand{position:absolute;left:14px;top:52px;font-size:10px;gap:5px}
  .card-front .brand-mark{width:11px;height:11px}
  .card-front .band{position:absolute;left:0;right:0;bottom:0;height:24px;background:var(--navy);border-top:1.5px solid var(--red);padding:2px 6px;display:flex;flex-direction:column;justify-content:center;align-items:center}
  .card-front .fine{font-size:4px}
</style>
</head>
<body>
<main class="stage">

  <section class="piece logo-card" aria-label="Logo">
    <div class="brand"><span class="brand-mark"></span>TR Claim Advisors</div>
  </section>

  <section class="piece letterhead" aria-label="Letterhead">
    <div class="brand"><span class="brand-mark"></span>TR Claim Advisors</div>
    <div class="band"><span class="fine">58 W. Alder St. Suite 612 Alder Falls, NY 11492 &nbsp; Tel 516.843.9075 x829 &nbsp; Fax 516.843.9075 &nbsp; www.trclaimpro.com</span></div>
  </section>

  <section class="piece envelope-back" aria-label="Envelope back">
    <svg viewBox="0 0 392 258" width="392" height="258" preserveAspectRatio="none">
      <defs>
        <linearGradient id="flapFill" x1="0" y1="0" x2="1" y2="1">
          <stop offset="0" stop-color="#2a6bc0"/>
          <stop offset="1" stop-color="#0b2a58"/>
        </linearGradient>
      </defs>
      <path d="M0 0 H392 V140 L270 110 Q230 100 190 112 L0 175 Z" fill="url(#flapFill)"/>
      <path d="M0 175 L190 112 Q230 100 270 110 L392 140" fill="none" stroke="#c4202e" stroke-width="1.5"/>
    </svg>
  </section>

  <section class="piece envelope-front" aria-label="Envelope front">
    <div class="brand"><span class="brand-mark"></span>TR Claim Advisors</div>
    <div class="band"><span class="fine">58 W. Alder St. Suite 612 Alder Falls, NY 11492</span></div>
  </section>

  <section class="piece card-back" aria-label="Business card back">
    <span class="brand-mark"></span>
  </section>

  <section class="piece card-front" aria-label="Business card front">
    <div class="person">
      <p class="name">Doran T. Whitcombe</p>
      <p class="role">Sr. Public Adjuster</p>
    </div>
    <div class="brand"><span class="brand-mark"></span>TR Claim Advisors</div>
    <div class="band">
      <span class="fine">58 W. Alder St. Suite 612 Alder Falls, NY 11492</span>
      <span class="fine">Tel 516.843.9075 x829 &nbsp; Fax 516.843.9075</span>
      <span class="fine">doran@trclaimpro.com &nbsp; www.trclaimpro.com</span>
    </div>
  </section>

</main>
</body>
</html>
```